Design home page for brightvane.xyz

We’re seeking a sleek, lead-generation-focused single-page website for Brightvane.xyz that communicates our expertise in delivering high-intent leads to mid-sized businesses. The goal is to guide visitors toward scheduling a free consultation while emphasizing our performance-based approach and comprehensive service offerings.

Industry/Entity Type

Marketing

Number of Pages Required

1 page

Font styles to use
Sans Serif

Requirements
Must have
• content from https://files.quorvalet.example/doc/7hTmwQRZa93KpLdVyxNe42UcBsFoGj8rYiMn5EkPtWz/view?tab=t.0
Nice to have
• color pallet from here https://files.quorvalet.example/doc/4pRkz-NWb62VxLeTyqJs8cHaDmFu3GiYoBnQ5tXeKv/view?tab=t.0

```html
<!DOCTYPE html>
<html lang="en">
<head>
<meta charset="utf-8">
<title>Brightvane.xyz – High-Intent Leads</title>
<link href="https://fonts.googleapis.com/css2?family=Poppins:wght@400;500;600;700;800&display=swap" rel="stylesheet">
<style>
:root{
  --navy:#0e1a33;
  --red:#c3122f;
  --orange:#f08a24;
  --ink:#2a2f3a;
  --muted:#5b6170;
  --soft:#f1f2f5;
  --line:#e3e5ea;
  --white:#ffffff;
}
*{box-sizing:border-box;margin:0;padding:0}
html,body{width:1200px;height:5148px;overflow:hidden}
body{font-family:'Poppins',sans-serif;color:var(--ink);background:var(--white)}
section,header,footer{position:relative;width:1200px;overflow:hidden}
.photo{position:absolute;border-radius:6px}
.btn{display:inline-block;background:var(--red);color:var(--white);font-weight:600;font-size:15px;padding:11px 24px;border-radius:4px}
.title{font-weight:700;color:var(--navy);font-size:44px;text-align:center;line-height:1.15}
.lead{text-align:center;font-size:15px;color:var(--muted);margin:12px auto 0;max-width:640px;line-height:1.5}
.stripe{position:absolute;left:0;width:1200px;height:40px}
.tick{display:inline-block;width:20px;height:20px;vertical-align:middle;margin-right:10px}

/* hero */
.hero{height:600px}
.brand{position:absolute;left:60px;top:22px;font-size:26px;font-weight:700;color:var(--navy)}
.hero .btn.top{position:absolute;right:60px;top:22px;font-size:13px;padding:9px 20px}
.hero-photo{left:560px;top:0;width:640px;height:540px;border-radius:0;background:linear-gradient(135deg,#cfd6e2,#8d99ae 55%,#4c5a72)}
.hero-copy{position:absolute;left:60px;top:110px;width:560px}
.hero h1{font-size:60px;font-weight:800;line-height:1.08;color:var(--navy)}
.hero h1 span{color:var(--red)}
.hero p{font-size:15px;font-weight:600;margin-top:22px;line-height:1.45;color:var(--ink);max-width:520px}
.hero .small{font-size:13px;font-weight:600;color:var(--red);margin-top:22px}
.hero .btn.main{margin-top:16px}

/* results */
.results{height:440px;padding-top:60px}
.trio{display:flex;justify-content:center;gap:60px;margin-top:48px}
.trio .item{width:300px;text-align:center}
.trio h3{font-size:20px;font-weight:700;color:var(--navy)}
.trio p{font-size:14px;color:var(--muted);margin-top:8px;line-height:1.5}

/* services */
.services{height:480px;background:var(--soft);padding-top:55px}
.cards{display:flex;justify-content:center;gap:14px;margin-top:40px}
.svc{position:relative;width:204px;height:250px;border-radius:8px;overflow:hidden}
.svc .fill{position:absolute;inset:0}
.svc .txt{position:absolute;left:16px;right:16px;bottom:18px;color:var(--white)}
.svc h4{font-size:18px;font-weight:700;line-height:1.2}
.svc p{font-size:12px;margin-top:6px;line-height:1.4;opacity:.9}

/* why */
.why{height:470px;padding-top:65px}
.boxes{display:flex;justify-content:center;gap:30px;margin-top:48px}
.box{width:330px;border:2px solid var(--red);border-radius:8px;padding:30px 24px;text-align:center}
.box .ico{width:56px;height:56px;margin:0 auto 14px}
.box h3{font-size:19px;color:var(--navy);font-weight:700}
.box p{font-size:13px;color:var(--muted);margin-top:8px;line-height:1.5}

/* tailored */
.tailored{height:520px;background:var(--soft);padding-top:55px}
.tl-grid{position:relative;height:330px;margin-top:36px}
.list{position:absolute;top:50px;list-style:none}
.list li{font-size:17px;font-weight:500;color:var(--navy);margin-bottom:20px}
.list.left{left:100px}
.list.right{left:875px}
.tl-photo{left:390px;top:0;width:420px;height:320px;background:linear-gradient(135deg,#b8c1cf,#5f6c83)}

/* how */
.how{height:640px;padding-top:60px}
.how-photo{left:90px;top:90px;width:470px;height:470px;border-radius:10px;background:linear-gradient(160deg,#d9dde5,#98a3b5 60%,#56637a)}
.how-copy{position:absolute;left:620px;top:80px;width:500px}
.how-copy .title,.grow-copy .title,.cta-copy .title{text-align:left}
.how-copy .lead,.grow-copy .lead{text-align:left;margin-left:0}
.step{display:flex;gap:16px;border:1px solid var(--line);border-left:4px solid var(--red);border-radius:8px;padding:18px;margin-top:20px;box-shadow:0 4px 14px rgba(14,26,51,.07)}
.step .ico{flex:0 0 44px;height:44px}
.step h3{font-size:18px;color:var(--red);font-weight:700}
.step p{font-size:13px;color:var(--muted);margin-top:4px;line-height:1.5}

/* growth */
.growth{height:670px;background:var(--soft)}
.grow-copy{position:absolute;left:60px;top:110px;width:480px}
.grow-photo{left:600px;top:110px;width:540px;height:460px;border-radius:10px;background:linear-gradient(135deg,#c79a6e,#8c6446 55%,#4c3a30)}
.pill{display:flex;gap:16px;background:var(--white);border-radius:8px;padding:18px;margin-top:22px;width:440px;box-shadow:0 4px 14px rgba(14,26,51,.07)}
.pill .ico{flex:0 0 44px;height:44px}
.pill h3{font-size:18px;color:var(--navy);font-weight:700}
.pill p{font-size:13px;color:var(--muted);margin-top:4px;line-height:1.5}

/* stories */
.stories{height:450px;padding-top:50px}
.quotes{display:flex;justify-content:center;gap:28px;margin-top:40px}
.quote{width:340px;border:1px solid var(--line);border-radius:8px;padding:22px;box-shadow:0 4px 14px rgba(14,26,51,.06)}
.who{display:flex;align-items:center;gap:12px}
.avatar{width:40px;height:40px;border-radius:50%;background:var(--red);color:var(--white);font-weight:700;display:flex;align-items:center;justify-content:center}
.who b{font-size:15px;color:var(--navy);display:block}
.stars{color:var(--orange);font-size:14px;letter-spacing:2px}
.quote p{font-size:13px;color:var(--muted);margin-top:12px;line-height:1.55}
.quote .role{font-size:12px;color:var(--red);font-weight:600;margin-top:10px}

/* cta */
.cta{height:630px;background:var(--soft)}
.cta-photo{left:60px;top:90px;width:560px;height:470px;border-radius:10px;background:linear-gradient(160deg,#d5d9e0,#9aa4b4 55%,#4e5b70)}
.cta-copy{position:absolute;left:670px;top:90px;width:470px}
.cta-copy .title{font-size:42px}
.cta-copy p{font-size:14px;color:var(--ink);margin-top:14px;line-height:1.55}
.cta-copy b{color:var(--navy)}
.cta-copy .btn{margin-top:22px}

/* footer */
.foot{height:248px;text-align:center;padding-top:70px}
.foot .name{font-size:34px;font-weight:700;color:var(--navy)}
.foot .tag{font-size:15px;color:var(--muted);margin-top:6px}
.foot .copy{font-size:12px;color:var(--muted);margin-top:36px}
</style>
</head>
<body>

<header class="hero">
  <div class="brand">brightvane.xyz</div>
  <span class="btn top">Schedule Your Call Now</span>
  <div class="photo hero-photo" role="img" aria-label="Team of business people celebrating success in an office"></div>
  <div class="hero-copy">
    <h1>High-Intent Leads Delivered Directly <span>To Your Pipeline.</span></h1>
    <p>Take The Guesswork Out Of Lead Generation. By Creating Visceral Connections With Your Audience, We Deliver High-Intent Prospects Who Are Genuinely Interested In What You Offer—Helping You Grow Your Sales Pipeline With Ease.</p>
    <div class="small">Let's Talk About How We Can Deliver The Leads Your Business Needs</div>
    <span class="btn main">Schedule Your Call Now</span>
  </div>
  <svg class="stripe" style="top:548px" viewBox="0 0 1200 40" preserveAspectRatio="none"><polygon points="0,30 1200,0 1200,12 0,40" fill="#c3122f"/><polygon points="0,22 380,13 380,18 0,28" fill="#0e1a33"/></svg>
</header>

<section class="results">
  <h2 class="title">We Deliver Results, Not Promises</h2>
  <p class="lead">At Brightvane.xyz, We Specialize In Providing Conversion-Ready Leads That Fuel Sustainable Business Growth.</p>
  <div class="trio">
    <div class="item"><h3>Entrepreneur-Led Expertise:</h3><p>Founded By Seasoned Entrepreneurs With Proven Lead Generation Success.</p></div>
    <div class="item"><h3>Performance-Based Model:</h3><p>No Upfront Costs—We Succeed Only When You Do.</p></div>
    <div class="item"><h3>Comprehensive Approach:</h3><p>From SEO To PPC Campaigns And High-Value Content Creation, We Manage It All.</p></div>
  </div>
  <svg class="stripe" style="top:395px" viewBox="0 0 1200 40" preserveAspectRatio="none"><polygon points="0,8 1200,28 1200,40 0,20" fill="#c3122f"/><polygon points="900,24 1200,29 1200,33 900,28" fill="#f08a24"/></svg>
</section>

<section class="services">
  <h2 class="title">Comprehensive End-To-End<br>Lead Generation</h2>
  <p class="lead">We Handle Everything Needed To Deliver High-Quality Leads So You Can Focus On Scaling Your Business.</p>
  <div class="cards">
    <div class="svc"><div class="fill" role="img" aria-label="Content creator recording video" style="background:linear-gradient(180deg,#7b5a4a,#1d1b22)"></div><div class="txt"><h4>Content Creation:</h4><p>Blogs, videos and lead magnets crafted to attract and convert.</p></div></div>
    <div class="svc"><div class="fill" role="img" aria-label="Designer working at a desk" style="background:linear-gradient(180deg,#a08670,#2a2420)"></div><div class="txt"><h4>Design &amp; Development:</h4><p>Conversion-ready sites and landing pages for maximum engagement.</p></div></div>
    <div class="svc"><div class="fill" role="img" aria-label="Laptop showing ad campaign dashboard" style="background:linear-gradient(180deg,#8a97a8,#1b2333)"></div><div class="txt"><h4>PPC Campaigns:</h4><p>Targeted paid search to drive qualified leads.</p></div></div>
    <div class="svc"><div class="fill" role="img" aria-label="Hands holding a phone with social apps" style="background:linear-gradient(180deg,#5d6f8a,#141c2b)"></div><div class="txt"><h4>SEO &amp; Social Media:</h4><p>Organic strategies to attract quality, high-intent leads.</p></div></div>
    <div class="svc"><div class="fill" role="img" aria-label="Analytics charts on a monitor" style="background:linear-gradient(180deg,#3a6e9a,#0f1a2c)"></div><div class="txt"><h4>Real-Time Optimization:</h4><p>Ongoing analysis and adjustments for peak performance and ROI.</p></div></div>
  </div>
</section>

<section class="why">
  <h2 class="title">Why Choose Brightvane.xyz?</h2>
  <p class="lead">We Specialize In Delivering High-Intent Leads That Drive Measurable Growth. Here's How We Stand Out:</p>
  <div class="boxes">
    <div class="box"><svg class="ico" viewBox="0 0 56 56"><rect x="4" y="4" width="48" height="48" rx="8" fill="#c3122f"/><polyline points="14,38 24,26 32,32 42,18" fill="none" stroke="#fff" stroke-width="3"/></svg><h3>Results-Driven Approach:</h3><p>We Handle All Aspects Of Lead Generation, From Creating Lead Magnets To Executing Advertising And SEO Campaigns, Delivering High-Quality Leads That Align With Your Goals.</p></div>
    <div class="box"><svg class="ico" viewBox="0 0 56 56"><rect x="4" y="4" width="48" height="48" rx="8" fill="#c3122f"/><circle cx="28" cy="28" r="12" fill="none" stroke="#fff" stroke-width="3"/><circle cx="28" cy="28" r="4" fill="#fff"/></svg><h3>Tailored Strategies:</h3><p>We Specialize In Creating Immersive, Visceral Connections That Resonate With Your Prospects, Establishing Trust And Interest From The Very First Interaction.</p></div>
    <div class="box"><svg class="ico" viewBox="0 0 56 56"><rect x="4" y="4" width="48" height="48" rx="8" fill="#c3122f"/><polyline points="16,29 25,37 40,20" fill="none" stroke="#fff" stroke-width="3.5"/></svg><h3>Simplified Growth Solutions:</h3><p>With All The Heavy Lifting Managed By Our Team, You Can Focus Entirely On Growing Your Business And Closing More Deals.</p></div>
  </div>
</section>

<section class="tailored">
  <h2 class="title">Tailored Content For High-Intent<br>Lead Capture</h2>
  <p class="lead">We Create Custom-Crafted Content Tailored For Your Audience:</p>
  <div class="tl-grid">
    <ul class="list left">
      <li><svg class="tick" viewBox="0 0 20 20"><polyline points="3,10 8,15 17,5" fill="none" stroke="#c3122f" stroke-width="3"/></svg>Guides And Ebooks</li>
      <li><svg class="tick" viewBox="0 0 20 20"><polyline points="3,10 8,15 17,5" fill="none" stroke="#c3122f" stroke-width="3"/></svg>Industry Insights Reports</li>
      <li><svg class="tick" viewBox="0 0 20 20"><polyline points="3,10 8,15 17,5" fill="none" stroke="#c3122f" stroke-width="3"/></svg>Infographics &amp; Visual Guides</li>
      <li><svg class="tick" viewBox="0 0 20 20"><polyline points="3,10 8,15 17,5" fill="none" stroke="#c3122f" stroke-width="3"/></svg>Glossary Of Industry Terms</li>
      <li><svg class="tick" viewBox="0 0 20 20"><polyline points="3,10 8,15 17,5" fill="none" stroke="#c3122f" stroke-width="3"/></svg>Checklist For Best Practices</li>
    </ul>
    <div class="photo tl-photo" role="img" aria-label="Two colleagues shaking hands in an office"></div>
    <ul class="list right">
      <li><svg class="tick" viewBox="0 0 20 20"><polyline points="3,10 8,15 17,5" fill="none" stroke="#c3122f" stroke-width="3"/></svg>Trend Spotting Forecast</li>
      <li><svg class="tick" viewBox="0 0 20 20"><polyline points="3,10 8,15 17,5" fill="none" stroke="#c3122f" stroke-width="3"/></svg>Templates And Toolkits</li>
      <li><svg class="tick" viewBox="0 0 20 20"><polyline points="3,10 8,15 17,5" fill="none" stroke="#c3122f" stroke-width="3"/></svg>Competitive Landscape</li>
      <li><svg class="tick" viewBox="0 0 20 20"><polyline points="3,10 8,15 17,5" fill="none" stroke="#c3122f" stroke-width="3"/></svg>Whitepapers</li>
    </ul>
  </div>
  <svg class="stripe" style="top:480px" viewBox="0 0 1200 40" preserveAspectRatio="none"><polygon points="800,30 1200,14 1200,22 800,38" fill="#f08a24"/></svg>
</section>

<section class="how">
  <div class="photo how-photo" role="img" aria-label="Business partners reviewing documents on a tablet"></div>
  <div class="how-copy">
    <h2 class="title">How We Deliver<br>High-Quality Leads</h2>
    <p class="lead">Our Streamlined Process Ensures You Receive Ready-To-Engage Leads Without The Hassle:</p>
    <div class="step"><svg class="ico" viewBox="0 0 44 44"><circle cx="22" cy="22" r="20" fill="#c3122f"/><circle cx="22" cy="22" r="9" fill="none" stroke="#fff" stroke-width="3"/></svg><div><h3>Precise Market Targeting:</h3><p>We Start By Understanding Your Ideal Customer Profile And Identifying High-Intent Prospects In Your Market.</p></div></div>
    <div class="step"><svg class="ico" viewBox="0 0 44 44"><circle cx="22" cy="22" r="20" fill="#c3122f"/><polyline points="13,28 20,20 26,25 32,15" fill="none" stroke="#fff" stroke-width="3"/></svg><div><h3>Customized Campaign Execution:</h3><p>We Take The Time To Understand Your Audience, Creating And Running Campaigns Tailored To Their Interests, Leveraging Insights From Advertising, SEO And Lead Magnets.</p></div></div>
    <div class="step"><svg class="ico" viewBox="0 0 44 44"><circle cx="22" cy="22" r="20" fill="#c3122f"/><polyline points="13,22 19,28 31,15" fill="none" stroke="#fff" stroke-width="3"/></svg><div><h3>All-Inclusive Management:</h3><p>From Strategy To Execution, We Handle Every Detail, Delivering Leads While You Focus On Closing Deals.</p></div></div>
  </div>
</section>

<section class="growth">
  <svg class="stripe" style="top:20px" viewBox="0 0 1200 40" preserveAspectRatio="none"><polygon points="0,10 600,30 600,38 0,18" fill="#c3122f"/></svg>
  <div class="grow-copy">
    <h2 class="title">Effortless Growth,<br>Designed For You</h2>
    <p class="lead">We Simplify Lead Generation, So You Can Focus On Growing Your Business:</p>
    <div class="pill"><svg class="ico" viewBox="0 0 44 44"><circle cx="22" cy="22" r="20" fill="#c3122f"/><polyline points="13,22 19,28 31,15" fill="none" stroke="#fff" stroke-width="3"/></svg><div><h3>Hands-Off Convenience:</h3><p>We Manage The Strategy, Content, Advertising, And Optimization, Delivering A Steady Flow Of High-Quality Prospects.</p></div></div>
    <div class="pill"><svg class="ico" viewBox="0 0 44 44"><circle cx="22" cy="22" r="20" fill="#c3122f"/><polyline points="13,30 20,22 26,26 32,14" fill="none" stroke="#fff" stroke-width="3"/></svg><div><h3>Built To Scale:</h3><p>Our Process Adapts To Your Growth Goals, Ensuring Consistent Lead Flow Whether You're Starting Small Or Scaling Rapidly.</p></div></div>
  </div>
  <div class="photo grow-photo" role="img" aria-label="Team collaborating around a table in a brick-walled office"></div>
</section>

<section class="stories">
  <h2 class="title">Proven Success Stories</h2>
  <p class="lead">Discover How Our Clients Have Achieved Exceptional Growth With Brightvane.xyz</p>
  <div class="quotes">
    <div class="quote"><div class="who"><div class="avatar">M</div><div><b>Marco T.</b><span class="stars">★★★★★</span></div></div><p>Brightvane.xyz has completely transformed our lead generation efforts. We've seen a 35% increase in high-quality leads in just three months.</p><div class="role">VP of Sales at a Mid-Sized B2B Firm</div></div>
    <div class="quote"><div class="who"><div class="avatar">P</div><div><b>Priya K.</b><span class="stars">★★★★★</span></div></div><p>The team at Brightvane.xyz took care of everything—from content to campaigns. Their performance-based model meant we only paid when results came in. It's a win-win!</p><div class="role">CEO of a Professional Services Company</div></div>
    <div class="quote"><div class="who"><div class="avatar">O</div><div><b>Owen B.</b><span class="stars">★★★★★</span></div></div><p>Working with Brightvane.xyz is like having an in-house growth team. Their ability to create and optimize content-driven campaigns helped us double our inbound inquiries.</p><div class="role">Marketing Director at a SaaS Company</div></div>
  </div>
</section>

<section class="cta">
  <div class="photo cta-photo" role="img" aria-label="Businesswoman working on a laptop in a bright office"></div>
  <div class="cta-copy">
    <h2 class="title">Ready To Unlock Scalable Growth For Your Business?</h2>
    <p>Schedule A Call To Learn How We Can Help Your Business Grow Predictably And Efficiently.</p>
    <p>Our Proven Strategies Are Tailored To Deliver:</p>
    <p><b>High-Intent Leads</b> that match your ideal customer profile.</p>
    <p><b>Custom Campaigns</b> designed to engage and convert your audience.</p>
    <p><b>Actionable Insights</b> to optimize performance and scale effectively.</p>
    <span class="btn">Schedule Your Call Now</span>
  </div>
</section>

<footer class="foot">
  <div class="name">brightvane.xyz</div>
  <div class="tag">Brightvane.xyz – Driving Real Growth, One Lead At A Time</div>
  <div class="copy">Copyright 2025 Brightvane.xyz LLC. All Rights Reserved.</div>
</footer>

</body>
</html>
```